Kestrel Appliance Care - Repair Plan Paperwork

Home Appliance Repair Agent and Repair Plan providing services to consumers' home appliances.

Pages Layout Guideline:
1) Introduction to KAC / Plan Schedule / Repair Plan Ref
2) Appliance Type / Model / Age / Cost of appliance within Repair Plan / Payment Schedule / Payment Dates / Amounts
3) Terms & Conditions

- Will also want a flyer design to go inside with the paperwork to market savings by adding additional products.

I have uploaded the logo, letterheads and website pages so you get a feel of the branding / design we use throughout.

```html
<!DOCTYPE html>
<html lang="en">
<head>
<meta charset="utf-8">
<title>Kestrel Appliance Care – Repair Plan Paperwork</title>
<link rel="stylesheet" href="https://fonts.googleapis.com/css2?family=Montserrat:wght@400;500;600;700&display=swap">
<style>
  :root{
    --orange:#f05a2a;
    --teal:#22b3bd;
    --ink:#3d3d3f;
    --grey:#5a5b5d;
    --paper:#ffffff;
    --stage:#e3e5e9;
  }
  *{box-sizing:border-box;margin:0;padding:0}
  html,body{width:1200px;height:1040px;overflow:hidden}
  body{background:var(--stage);font-family:'Montserrat',sans-serif;color:var(--ink);position:relative}

  .page{position:absolute;top:258px;width:370px;height:524px;background:var(--paper);overflow:hidden;box-shadow:0 6px 18px rgba(0,0,0,.18)}
  .page--intro{left:30px}
  .page--payments{left:415px}
  .page--flyer{left:800px}
  .page-bg{position:absolute;inset:0;width:370px;height:524px}
  .page > *:not(.page-bg){position:absolute}

  .heading{font-weight:700;font-size:11.5px;color:var(--orange);letter-spacing:.2px;line-height:1.15;text-transform:uppercase;white-space:nowrap}
  .heading--large{font-size:14.5px}
  .heading--small{font-size:10px;letter-spacing:0}
  .heading--light{color:#fff}
  .heading .accent{color:var(--teal)}
  .body-text{font-size:5.8px;line-height:1.35;color:var(--ink);text-align:justify}
  .body-text p + p{margin-top:5px}
  .body-text--light{color:#fff;text-align:left}

  .photo{border-radius:50%;border:2.5px solid var(--orange);overflow:hidden}
  .photo--repair{background:radial-gradient(circle at 60% 45%,#3b5aa8 0 18%,#6d6f75 40%,#c9ccd1 85%)}
  .photo--kitchen{background:linear-gradient(160deg,#f4f4f2 0%,#d9dcdf 50%,#8f9499 100%)}
  .photo--lounge{background:linear-gradient(170deg,#f3f1ee 0%,#e4ded5 55%,#b9a58e 100%)}
  .photo--technician{background:radial-gradient(circle at 55% 45%,#4b4f57 0 25%,#7d838c 55%,#c7cbd0 90%)}
  .photo--washer{background:radial-gradient(circle,#f7c9c4,#e98a84)}
  .photo--dishwasher{background:radial-gradient(circle,#ffffff,#d3d6da)}
  .photo--fridge{background:radial-gradient(circle,#cfe9f7,#5fb6e6)}

  .brand{left:20px;top:46px;color:var(--grey);font-weight:600;line-height:1}
  .brand__name{font-size:36px;letter-spacing:1px}
  .brand__tag{font-size:10.5px;letter-spacing:3.4px;margin-top:4px;padding-left:20px}

  .feature{display:flex;gap:7px;width:170px;align-items:flex-start}
  .feature__icon{flex:0 0 28px;height:28px;border-radius:50%;background:#fff;border:1.5px solid var(--orange);display:flex;align-items:center;justify-content:center}
  .feature__title{font-size:5.6px;font-weight:700;color:#fff;text-transform:uppercase;margin:3px 0 3px}
  .feature__text{font-size:4.8px;line-height:1.4;color:#fff}

  .step{width:94px;text-align:center;top:62px}
  .step__icon{width:33px;height:33px;margin:0 auto;border-radius:50%;border:1.5px solid var(--orange);background:#fff;display:flex;align-items:center;justify-content:center}
  .step__label{font-size:5.4px;font-weight:700;color:var(--teal);margin:4px 0 2px}
  .step__text{font-size:4.6px;line-height:1.35}

  .appliance{width:80px;text-align:center;top:60px}
  .appliance .photo{width:64px;height:64px;margin:0 auto;border-width:2px}
  .appliance__label{font-size:5.4px;font-weight:600;margin-top:9px;text-transform:uppercase}
  .make{top:155px;width:56px;height:23px;border:1px solid #cfd2d6;background:#fff;display:flex;align-items:center;justify-content:center;font-size:8px;font-weight:700;color:var(--grey);letter-spacing:.4px;text-transform:uppercase}

  .footer{font-size:6px;line-height:1.6;color:#fff;top:496px}
</style>
</head>
<body>

<section class="page page--intro">
  <svg class="page-bg" viewBox="0 0 370 524" aria-hidden="true">
    <path d="M0,0 H370 V282 L342,254 V56 Q342,28 314,28 H28 Z" fill="var(--orange)"/>
    <path d="M0,270 H125 L190,330 V500 H0 Z" fill="var(--teal)"/>
  </svg>

  <div class="brand">
    <div class="brand__name">KESTREL</div>
    <div class="brand__tag">APPLIANCE CARE</div>
  </div>
  <div class="photo photo--repair" style="left:214px;top:38px;width:124px;height:124px;border-color:#555" role="img" aria-label="Technician repairing a fridge-freezer in a kitchen"></div>

  <h2 class="heading" style="left:11px;top:120px">Welcome to KAC</h2>
  <div class="body-text" style="left:11px;top:136px;width:205px">
    <p>Lorem ipsum dolor sit amet, consectetuer adipiscing elit, sed diam nonummy nibh euismod tincidunt ut laoreet dolore magna aliquam erat volutpat. Ut wisi enim ad minim veniam, quis nostrud exerci tation ullamcorper suscipit lobortis nisl ut aliquip ex ea commodo consequat. Duis autem vel eum iriure dolor in hendrerit in vulputate velit esse molestie consequat.</p>
  </div>
  <div class="body-text" style="left:11px;top:198px;width:300px">
    <p>vel illum dolore eu feugiat nulla facilisis at vero eros et accumsan et iusto odio dignissim qui blandit praesent luptatum zzril delenit augue duis dolore te feugait nulla facilisi. Lorem ipsum dolor sit amet, cons ectetuer adipiscing elit, sed diam nonummy nibh euismod tincidunt ut laoreet dolore magna aliquam erat volutpat.</p>
    <p>Lorem ipsum dolor sit amet, cons ectetuer adipiscing elit, sed diam nonummy nibh euismod tincidunt ut laoreet dolore magna aliquam erat volutpat.</p>
  </div>

  <h2 class="heading heading--light" style="left:10px;top:290px">Whats included<br>with KAC?</h2>
  <div class="feature" style="left:9px;top:327px">
    <div class="feature__icon"><svg width="16" height="16" viewBox="0 0 16 16" fill="none" stroke="var(--orange)" stroke-width="1.2"><circle cx="8" cy="8" r="3"/><path d="M8 1v2.5M8 12.5V15M1 8h2.5M12.5 8H15M3 3l1.8 1.8M11.2 11.2 13 13M13 3l-1.8 1.8M4.8 11.2 3 13"/></svg></div>
    <div><div class="feature__title">Technical support</div><div class="feature__text">Tempor incididunt ut labore et dolore magna aliqua. Ut enim ad minim veniam, quis nost rud exercitation ullamco laboris nisi ut aliquip.</div></div>
  </div>
  <div class="feature" style="left:9px;top:385px">
    <div class="feature__icon"><svg width="16" height="16" viewBox="0 0 16 16" fill="none" stroke="var(--orange)" stroke-width="1.2"><circle cx="8" cy="8" r="6"/><path d="M5 11l4-4M9 7a2 2 0 1 0 2-2"/></svg></div>
    <div><div class="feature__title">Quick repairs</div><div class="feature__text">Tempor incididunt ut labore et dolore magna aliqua. Ut enim ad minim veniam, quis nost rud exercitation ullamco laboris nisi ut aliquip.</div></div>
  </div>
  <div class="feature" style="left:9px;top:442px">
    <div class="feature__icon"><svg width="16" height="16" viewBox="0 0 16 16" fill="none" stroke="var(--orange)" stroke-width="1.2"><path d="M5 2h6v4a3 3 0 0 1-6 0zM5 3H2.5a2.5 2.5 0 0 0 2.5 3M11 3h2.5A2.5 2.5 0 0 1 11 6M8 9v3M5 14h6"/></svg></div>
    <div><div class="feature__title">Competitive prices</div><div class="feature__text">Tempor incididunt ut labore et dolore magna aliqua. Ut enim ad minim veniam, quis nost rud exercitation ullamco laboris nisi ut aliquip.</div></div>
  </div>

  <h2 class="heading" style="left:204px;top:276px">Plan details</h2>
  <div class="body-text" style="left:204px;top:292px;width:156px">
    <p>vel illum dolore eu feugiat nulla facilisis at vero eros et accumsan et iusto odio dignissim qui blandit praesent luptatum zzril delenit augue duis dolore te feugait nulla facilisi. Lorem ipsum dolor sit amet, cons ectetuer adipiscing elit, sed diam nonummy nibh euismod tincidunt ut laoreet dolore magna aliquam erat volutpat.</p>
    <p>Lorem ipsum dolor sit amet, cons ectetuer adipiscing elit, sed diam nonummy nibh euismod tincidunt ut laoreet dolore magna aliquam erat volutpat.</p>
  </div>
  <div class="photo photo--kitchen" style="left:248px;top:400px;width:120px;height:120px" role="img" aria-label="Bright modern kitchen with fitted appliances"></div>

  <svg class="page-bg" viewBox="0 0 370 524" aria-hidden="true" style="z-index:1"><path d="M0,524 V510 Q8,490 36,488 H370 V524 Z" fill="var(--orange)"/></svg>
  <div class="footer" style="left:102px;z-index:2">123, Lorem ipsum dolor sit amet,<br>tetur adipiscing elit</div>
  <div class="footer" style="left:245px;z-index:2">Phone : +1 888 888 8888<br>Email : info@companyname.com</div>
</section>

<section class="page page--payments">
  <svg class="page-bg" viewBox="0 0 370 524" aria-hidden="true">
    <path d="M0,0 H370 V252 L338,220 V56 Q338,28 310,28 H28 Z" fill="var(--orange)"/>
    <path d="M0,232 H145 L190,277 V500 H0 Z" fill="var(--teal)"/>
  </svg>

  <h2 class="heading heading--large" style="left:18px;top:40px">Simple booking process</h2>
  <div class="step" style="left:12px">
    <div class="step__icon"><svg width="18" height="18" viewBox="0 0 18 18" fill="none" stroke="var(--teal)" stroke-width="1.2"><circle cx="9" cy="7" r="3.2"/><path d="M4 7a5 5 0 0 1 10 0M3 17a6 5 0 0 1 12 0"/></svg></div>
    <div class="step__label">STEP 01</div>
    <div class="step__text">Tempor incididunt ut labore et dolore magna aliqua. Ut enim ad minim veniam, quis nost rud exercitation ullamco laboris nisi ut aliquip.</div>
  </div>
  <div class="step" style="left:124px">
    <div class="step__icon"><svg width="18" height="18" viewBox="0 0 18 18" fill="none" stroke="var(--teal)" stroke-width="1.2"><rect x="3" y="3.5" width="12" height="11" rx="1"/><path d="M3 7h12M6 2v3M12 2v3M6 10h1M9 10h1M12 10h1M6 12.5h1M9 12.5h1"/></svg></div>
    <div class="step__label">STEP 02</div>
    <div class="step__text">Tempor incididunt ut labore et dolore magna aliqua. Ut enim ad minim veniam, quis nost rud exercitation ullamco laboris nisi ut aliquip.</div>
  </div>
  <div class="step" style="left:236px">
    <div class="step__icon"><svg width="18" height="18" viewBox="0 0 18 18" fill="none" stroke="var(--teal)" stroke-width="1.2"><path d="M5 7a4 4 0 0 1 8 0zM6 8a3 3 0 0 0 6 0M3 17a6 5 0 0 1 12 0"/></svg></div>
    <div class="step__label">STEP 03</div>
    <div class="step__text">Tempor incididunt ut labore et dolore magna aliqua. Ut enim ad minim veniam, quis nost rud exercitation ullamco laboris nisi ut aliquip.</div>
  </div>

  <h2 class="heading" style="left:20px;top:161px">Payment dates</h2>
  <div class="body-text" style="left:20px;top:177px;width:216px">
    <p>Lorem ipsum dolor sit amet, consectetuer adipiscing elit, sed diam nonummy nibh euismod tincidunt ut laoreet dolore magna aliquam erat volutpat. Ut wisi enim ad minim veniam, quis nostrud exerci tation ullamcorper suscipit lobortis nisl ut aliquip ex ea commodo consequat. Duis autem vel eum iriure dolor in hendrerit in vulputate velit esse molestie consequat.</p>
  </div>
  <div class="photo photo--kitchen" style="left:258px;top:142px;width:88px;height:88px" role="img" aria-label="Open-plan kitchen and dining room"></div>

  <h2 class="heading heading--light" style="left:21px;top:271px">Cover details</h2>
  <div class="body-text body-text--light" style="left:21px;top:287px;width:132px">
    <p>Lorem ipsum dolor sit amet, consectetuer adipiscing elit, sed diam nonummy nibh euismod tincidunt ut laoreet dolore magna aliquam erat volutpat. Ut wisi enim ad minim veniam, quis nostrud exerci tation ullamcorper suscipit lobortis nisl ut aliquip ex ea commodo consequat. Duis autem vel eum iriure dolor in hendrerit in vulputate velit esse molestie consequat.</p>
    <p>vel illum dolore eu feugiat nulla facilisis at vero eros et accumsan et iusto odio dignissim qui blandit praesent luptatum zzril delenit augue duis dolore te feugait nulla facilisi.</p>
  </div>

  <h2 class="heading" style="left:199px;top:275px">Payment schedule</h2>
  <div class="body-text" style="left:199px;top:291px;width:161px">
    <p>Lorem ipsum dolor sit amet, consectetuer adipiscing elit, sed diam nonummy nibh euismod tincidunt ut laoreet dolore magna aliquam erat volutpat. Ut wisi enim ad minim veniam, quis nostrud exerci tation ullamcorper suscipit lobortis nisl ut aliquip ex ea commodo consequat. Duis autem vel eum iriure dolor in hendrerit in vulputate velit esse molestie consequat.</p>
    <p>Ut wisi enim ad minim veniam, quis nostrud exerci tation ullamcorper suscipit lobortis nisl ut aliquip ex ea commodo consequat. Duis autem vel eum iriure dolor in hendrerit in vulputate velit esse molestie consequat.</p>
  </div>
  <div class="photo photo--lounge" style="left:268px;top:402px;width:92px;height:92px" role="img" aria-label="Homeowner relaxing on a sofa"></div>

  <svg class="page-bg" viewBox="0 0 370 524" aria-hidden="true" style="z-index:1"><path d="M0,524 V510 Q8,490 36,488 H370 V524 Z" fill="var(--orange)"/></svg>
  <div class="footer" style="left:102px;z-index:2">123, Lorem ipsum dolor sit amet,<br>tetur adipiscing elit</div>
  <div class="footer" style="left:245px;z-index:2">Phone : +1 888 888 8888<br>Email : info@companyname.com</div>
</section>

<section class="page page--flyer">
  <svg class="page-bg" viewBox="0 0 370 524" aria-hidden="true">
    <path d="M0,0 H370 V230 L342,202 V56 Q342,28 314,28 H28 Z" fill="var(--orange)"/>
    <path d="M0,234 H150 L190,272 V500 H0 Z" fill="var(--teal)"/>
  </svg>

  <h2 class="heading" style="left:26px;top:42px">Appliance type we <span class="accent">repair</span></h2>
  <div class="appliance" style="left:20px">
    <div class="photo photo--washer" role="img" aria-label="Washing machines and laundry appliances"></div>
    <div class="appliance__label">Washing machines</div>
  </div>
  <div class="appliance" style="left:134px">
    <div class="photo photo--dishwasher" role="img" aria-label="Stainless steel dishwasher"></div>
    <div class="appliance__label">Dishwashers</div>
  </div>
  <div class="appliance" style="left:246px">
    <div class="photo photo--fridge" role="img" aria-label="Open fridge-freezer stocked with food"></div>
    <div class="appliance__label">Fridge-freezers</div>
  </div>

  <div class="make" style="left:23px">Norvik</div>
  <div class="make" style="left:104px">Halden</div>
  <div class="make" style="left:185px">Corvell</div>
  <div class="make" style="left:266px">Sterlux</div>

  <h2 class="heading heading--small" style="left:202px;top:220px"><span class="accent">Save money by adding</span><br>more appliances!</h2>
  <div class="body-text" style="left:202px;top:248px;width:155px">
    <p>Lorem ipsum dolor sit amet, consectetuer adipiscing elit, sed diam nonummy nibh euismod tincidunt ut laoreet dolore magna aliquam erat volutpat. Ut wisi enim ad minim veniam, quis nostrud exerci tation ullamcorper suscipit lobortis nisl ut aliquip ex ea commodo consequat. Duis autem vel eum iriure dolor in hendrerit in vulputate velit esse molestie consequat.</p>
    <p>Lorem ipsum dolor sit amet, consectetuer adipiscing elit, sed diam nonummy nibh euismod tincidunt ut laoreet dolore magna aliquam erat volutpat. Ut wisi enim ad minim veniam, quis nostrud exerci tation ullamcorper suscipit lobortis nisl ut aliquip ex ea commodo consequat. Duis autem vel eum iriure dolor in hendrerit in vulputate velit esse molestie consequat.</p>
  </div>

  <div class="body-text body-text--light" style="left:21px;top:262px;width:150px">
    <p>Lorem ipsum dolor sit amet, consectetuer adipiscing elit, sed diam nonummy nibh euismod tincidunt ut laoreet dolore magna aliquam erat volutpat. Ut wisi enim ad minim veniam, quis nostrud exerci tation ullamcorper suscipit lobortis nisl ut aliquip ex ea commodo consequat. Duis autem vel eum iriure dolor in hendrerit in vulputate velit esse molestie consequat.</p>
    <p>vel illum dolore eu feugiat nulla facilisis at vero eros et accumsan et iusto odio dignissim qui blandit praesent luptatum zzril delenit augue duis dolore te feugait nulla facilisi. Lorem ipsum dolor sit amet, cons ectetuer adipiscing elit, sed diam nonummy nibh euismod tincidunt ut laoreet dolore magna aliquam erat volutpat.</p>
    <p>vel illum dolore eu feugiat nulla facilisis at vero eros et accumsan et iusto odio dignissim qui blandit praesent luptatum zzril delenit augue duis dolore te feugait nulla facilisi. Lorem ipsum dolor sit amet, cons ectetuer adipiscing elit, sed diam nonummy nibh euismod tincidunt ut laoreet dolore magna aliquam erat volutpat.</p>
  </div>
  <div class="photo photo--technician" style="left:264px;top:396px;width:96px;height:96px" role="img" aria-label="Engineer servicing an appliance"></div>

  <svg class="page-bg" viewBox="0 0 370 524" aria-hidden="true" style="z-index:1"><path d="M0,524 V510 Q8,490 36,488 H370 V524 Z" fill="var(--orange)"/></svg>
  <div class="footer" style="left:102px;z-index:2">123, Lorem ipsum dolor sit amet,<br>tetur adipiscing elit</div>
  <div class="footer" style="left:245px;z-index:2">Phone : +1 888 888 8888<br>Email : info@companyname.com</div>
</section>

</body>
</html>
```